Deactivated Coal-Fired Power Plant to be redeveloped into a Green Energy Campus.

Want a striking business card statement that introduces our concept project to provide economic and community recovery to a former rural coal community in western PA.
Essentially 12 project representatives that will lead both the demolition of an existing power plant and the redevelopment to a new Green energy site.
Business Card should reflect our effort.
We are open to ideas.

Target Market(s)

Energy and Power Generation industries

Industry/Entity Type

Power Generation and Data Centers

Contact Information for Business Card

Included in uploaded materials

Font styles to use
Sans Serif
Other font styles liked:
• Arial, Calibri

Requirements
Must have
• Multiple colors

```html
<!DOCTYPE html>
<html lang="en">
<head>
<meta charset="utf-8">
<title>Ridgeline Renewal – Business Card</title>
<link href="https://fonts.googleapis.com/css2?family=Montserrat:wght@500;600;700;800&display=swap" rel="stylesheet">
<style>
  :root{
    --green:#16923f;
    --green-pale:#b9dcc0;
    --green-mid:#8fbf96;
    --ink:#141414;
    --paper:#ffffff;
    --backdrop:#e9ece9;
  }
  *{box-sizing:border-box;margin:0;padding:0}
  html,body{width:1200px;height:801px;overflow:hidden}
  body{
    background:var(--backdrop);
    font-family:"Montserrat",Arial,sans-serif;
    position:relative;
  }
  .card{
    position:absolute;
    top:246px;
    width:540px;
    height:309px;
    border-radius:14px;
    overflow:hidden;
    box-shadow:0 6px 18px rgba(0,0,0,.18);
    border-bottom:3px solid var(--green);
  }
  .card--brand{left:36px}
  .card--contact{left:624px;background:var(--paper)}

  .site-photo{
    position:absolute;inset:0;
    background:linear-gradient(160deg,var(--green-pale) 0%,#a6cfac 45%,var(--green-mid) 100%);
  }
  .wordmark{
    position:absolute;
    display:flex;align-items:center;gap:14px;
  }
  .wordmark__dot{
    border-radius:50%;
    background:var(--green);
    flex:none;
  }
  .wordmark__name{
    font-weight:800;
    color:var(--ink);
    text-transform:uppercase;
    line-height:1;
    letter-spacing:.5px;
  }
  .card--brand .wordmark{left:50%;top:50%;transform:translate(-50%,-50%)}
  .card--brand .wordmark__dot{width:64px;height:64px}
  .card--brand .wordmark__name{font-size:38px}

  .card--contact .wordmark{left:30px;top:50%;transform:translateY(-50%);gap:10px}
  .card--contact .wordmark__dot{width:40px;height:40px}
  .card--contact .wordmark__name{font-size:21px}

  .divider{
    position:absolute;left:262px;top:46px;
    width:1px;height:218px;background:var(--ink);
  }
  .details{
    position:absolute;left:282px;top:52px;right:18px;
    color:var(--ink);
  }
  .details__name{
    color:var(--green);font-weight:800;font-size:21px;
    letter-spacing:.5px;text-transform:uppercase;line-height:1.1;
  }
  .details__role{font-size:12px;font-weight:500;margin-top:4px}
  .details__company{color:var(--green);font-size:12px;font-weight:600;margin-top:14px}
  .details__place{font-size:12px;font-weight:500;margin-top:3px}
  .contact-list{list-style:none;margin-top:16px}
  .contact-list li{
    display:flex;align-items:center;gap:8px;
    font-size:12.5px;font-weight:500;margin-top:6px;white-space:nowrap;
  }
  .contact-list .is-green{color:var(--green)}
  .contact-list svg{width:13px;height:13px;flex:none;fill:var(--green)}
</style>
</head>
<body>
  <section class="card card--brand">
    <div class="site-photo" role="img" aria-label="Faded aerial view of the power plant site and surrounding green hills"></div>
    <div class="wordmark">
      <span class="wordmark__dot"></span>
      <span class="wordmark__name">Ridgeline Renewal</span>
    </div>
  </section>

  <section class="card card--contact">
    <div class="wordmark">
      <span class="wordmark__dot"></span>
      <span class="wordmark__name">Ridgeline<br>Renewal</span>
    </div>
    <div class="divider"></div>
    <div class="details">
      <h1 class="details__name">Daniel Marchetti</h1>
      <p class="details__role">Chief Operation Officer</p>
      <p class="details__company">Ridgeline Renewal LLC</p>
      <p class="details__place">Alder Falls, Pennsylvania</p>
      <ul class="contact-list">
        <li>
          <svg viewBox="0 0 24 24" aria-hidden="true"><path d="M6.6 10.8a15.1 15.1 0 0 0 6.6 6.6l2.2-2.2c.3-.3.7-.4 1-.2 1.1.4 2.3.6 3.6.6.6 0 1 .4 1 1V20c0 .6-.4 1-1 1A17 17 0 0 1 3 4c0-.6.4-1 1-1h3.5c.6 0 1 .4 1 1 0 1.3.2 2.5.6 3.6.1.3 0 .7-.2 1z"/></svg>
          555.214.0180
        </li>
        <li>
          <svg viewBox="0 0 24 24" aria-hidden="true"><path d="M7 1h10a2 2 0 0 1 2 2v18a2 2 0 0 1-2 2H7a2 2 0 0 1-2-2V3a2 2 0 0 1 2-2zm0 3v14h10V4zm5 15.5a1 1 0 1 0 0 2 1 1 0 0 0 0-2z"/></svg>
          555.386.2740
        </li>
        <li class="is-green">
          <svg viewBox="0 0 24 24" aria-hidden="true"><path d="M2 5h20v14H2zm2 2v.5l8 5 8-5V7zm0 2.8V17h16V9.8l-8 5z"/></svg>
          dmarchetti@ridgelinerenewal.com
        </li>
        <li>
          <svg viewBox="0 0 24 24" aria-hidden="true"><path d="M12 2a10 10 0 1 0 0 20 10 10 0 0 0 0-20zm6.9 6h-3a15 15 0 0 0-1.3-3.9A8 8 0 0 1 18.9 8zM12 4c.8 1.2 1.5 2.5 1.9 4h-3.8c.4-1.5 1.1-2.8 1.9-4zM4.3 14a8 8 0 0 1 0-4h3.4a16 16 0 0 0 0 4zm.8 2h3a15 15 0 0 0 1.3 3.9A8 8 0 0 1 5.1 16zm3-8h-3a8 8 0 0 1 4.3-3.9A15 15 0 0 0 8.1 8zM12 20c-.8-1.2-1.5-2.5-1.9-4h3.8c-.4 1.5-1.1 2.8-1.9 4zm2.3-6H9.7a14 14 0 0 1 0-4h4.6a14 14 0 0 1 0 4zm.3 5.9a15 15 0 0 0 1.3-3.9h3a8 8 0 0 1-4.3 3.9zm1.7-5.9a16 16 0 0 0 0-4h3.4a8 8 0 0 1 0 4z"/></svg>
          ridgelinerenewal.com
        </li>
      </ul>
    </div>
  </section>
</body>
</html>
```